Medical equipment business looking for professional, unique business card

We need a business card design for a durable medical equipment company. We are small but would like our cards to express that we are much bigger. We focus on braces (back, knee, wrist, etc) but also do crutches, rollators, wheelchairs- basically medical equipment that gets you going and back in Action. Our colors are blue and green and our logo has an arrow and use of a "spine". We'd like to express professionalism while being unique.

Industry/Entity Type

Medical Equipment

Contact Information for Business Card

Professional feel but unique. Memorable.

Font styles to use
Serif
Sans Serif
Other font styles liked:
• verdana

Requirements
Must have
• card holders cell#, business phone#, fax#, email, website address, business address, logo
Nice to have
• use of medical/healthcare related descriptive words, items, look
Should not have
• the wrong colors or cartoon characters.

```html
<!DOCTYPE html>
<html lang="en">
<head>
<meta charset="utf-8">
<title>Kinetra Medical – Business Card</title>
<link rel="stylesheet" href="https://fonts.googleapis.com/css2?family=Arimo:wght@400;700&display=swap">
<style>
  :root {
    --backdrop: #5b4a3b;
    --card-white: #ffffff;
    --brand-navy: #0c4a6e;
    --brand-green: #8dc63f;
    --text-grey: #4a4a4a;
    --rule-grey: #a9a9a9;
  }
  html, body {
    margin: 0;
    padding: 0;
    width: 1200px;
    height: 987px;
    overflow: hidden;
    background: var(--backdrop);
    font-family: "Arimo", Arial, sans-serif;
  }
  .card {
    position: absolute;
    left: 293px;
    width: 615px;
    height: 352px;
    box-shadow: 0 2px 6px rgba(0,0,0,0.35);
  }
  .card--front { top: 130px; background: var(--card-white); }
  .card--back  { top: 505px; background: var(--brand-green); }

  .brand {
    position: absolute;
    left: 0; right: 0;
    display: flex;
    justify-content: center;
    align-items: center;
    gap: 12px;
    color: var(--brand-navy);
    font-weight: 700;
    font-size: 44px;
    letter-spacing: -0.5px;
  }
  .brand__dot {
    width: 16px; height: 16px;
    border-radius: 50%;
    background: var(--brand-green);
  }
  .card--front .brand { top: 44px; }
  .card--back .brand { top: 150px; }
  .card--back .brand__dot { background: var(--brand-navy); }

  .rule {
    position: absolute;
    left: 32px;
    width: 548px;
    height: 1px;
    background: var(--rule-grey);
  }
  .rule--top { top: 180px; }
  .rule--bottom { top: 293px; }

  .holder {
    position: absolute;
    left: 32px;
    top: 188px;
  }
  .holder__name {
    margin: 0;
    font-size: 22px;
    font-weight: 400;
    color: var(--brand-navy);
  }
  .holder__title {
    margin: 3px 0 0;
    font-size: 16px;
    color: var(--brand-green);
  }
  .holder__address {
    margin: 14px 0 0;
    font-size: 15px;
    line-height: 21px;
    color: var(--text-grey);
    font-style: normal;
  }

  .contacts {
    position: absolute;
    right: 32px;
    top: 193px;
    margin: 0;
    padding: 0;
    list-style: none;
  }
  .contacts li {
    display: flex;
    justify-content: flex-end;
    align-items: center;
    gap: 10px;
    height: 24px;
    font-size: 15px;
    color: var(--text-grey);
  }
  .contacts svg {
    width: 17px;
    height: 17px;
    fill: var(--brand-navy);
  }

  .website {
    position: absolute;
    left: 0; right: 0;
    top: 309px;
    text-align: center;
    font-size: 14px;
    font-weight: 700;
    letter-spacing: 5px;
    color: var(--brand-navy);
  }
</style>
</head>
<body>

<section class="card card--front">
  <div class="brand"><span class="brand__dot"></span>Kinetra Medical</div>

  <div class="rule rule--top"></div>

  <div class="holder">
    <h1 class="holder__name">Daniel Marsh</h1>
    <p class="holder__title">President</p>
    <address class="holder__address">2190 Alder Lane<br>Brookfield, NY 11020</address>
  </div>

  <ul class="contacts">
    <li>555 0142 7781
      <svg viewBox="0 0 16 16" aria-label="Office phone"><path d="M2 6c0-2 3-4 6-4s6 2 6 4v1h-3V5.5C10 5 9 4.8 8 4.8S6 5 5 5.5V7H2z"/><rect x="3" y="8" width="10" height="6" rx="1"/></svg>
    </li>
    <li>555 0193 4406
      <svg viewBox="0 0 16 16" aria-label="Mobile"><path d="M4.5 1h7a1 1 0 0 1 1 1v12a1 1 0 0 1-1 1h-7a1 1 0 0 1-1-1V2a1 1 0 0 1 1-1zm.8 2v9h5.4V3z"/></svg>
    </li>
    <li>555 0178 2259
      <svg viewBox="0 0 16 16" aria-label="Fax"><rect x="4" y="1" width="8" height="5"/><rect x="1" y="6" width="14" height="6" rx="1"/><rect x="4" y="10" width="8" height="5" fill="#fff" stroke="#0c4a6e" stroke-width="1.2"/></svg>
    </li>
    <li>dan@kinetramed.com
      <svg viewBox="0 0 16 16" aria-label="Email"><path d="M1 3h14v10H1z"/><path d="M1 3l7 5 7-5" fill="none" stroke="#fff" stroke-width="1.2"/></svg>
    </li>
  </ul>

  <div class="rule rule--bottom"></div>

  <div class="website">www.kinetramed.com</div>
</section>

<section class="card card--back">
  <div class="brand"><span class="brand__dot"></span>Kinetra Medical</div>
</section>

</body>
</html>
```